Creative designer wanted for unique pet treats product packaging!

My company is "Tailwag Pantry!" and we're a new and upcoming premium pet treat company. We are different than the rest as we have core values that really stand out and that we're VERY passionate about. They are the following:
HEALTHY-All of our ingredients are fresh and wholesome for dogs. Each has unique health benefits for dogs and there is never any filler-just the good stuff.
AMOUNT OF INGREDIENTS-Most of dog treats have large lists of ingredients and often many of those are difficult to pronounce or people have to look up what they even are. Often there is lot of "filler". We pride ourselves on just having a few ingredients or less. Every ingredient can easily be pronounced, recognized and are commonly consumed by humans in regular meals.
GIVING BACK- We donate a portion of the proceeds of every bag to go to hand selected, accredited and legit animals charities and rescues.
ENVIRONMENT- We strongly care about the environment which is why our bags are compostable. Just simply remove the zipper and track then put the bag in a composting bin. Easy as that. (We have attached a "how to compost your bag in 2 simple steps" image that we would like shown on the bags.
Our initial product is Maple Sage Crunchy Bark-ley Bites. The ingredients are: Coconut oil, dill, and sweet potato.
We want a design that embodies our values. As well, we have attached "our story" that describes the company and what we are about to consumers. We would like to have it put on the package, but if it cannot be done, then just the meat and potatoes of the message.
A good example for recognition is the attached cake mix as it's simple, portrays the product nicely and when seen from afar-it is easily identified.
*We would like to have a window on the bag that is similar to our paw and leaf logo.
We would also like to see the color green on the package.
Bag specifics are:
Size: 250g OPTIMIZED
Dimensions Inches: 6.15''x9.41''x3.50''
Dimensions mm : 156x239x89
Type: Stand-Up Pouch with Zip (PLOW)
COMPOSTABLE
Material: 100NK MATTE/70NKA/3mil BIOPBS
CMYKW

```html
<!DOCTYPE html>
<html lang="en">
<head>
<meta charset="utf-8">
<title>Tailwag Pantry! – Maple Sage Crunchy Bark-ley Bites pouch</title>
<link rel="stylesheet" href="https://fonts.googleapis.com/css2?family=Arvo:wght@400;700&family=Sacramento&display=swap">
<style>
  :root {
    --leaf-green: #8dc63f;
    --stripe-green: #7cb733;
    --forest-green: #006633;
    --bark-brown: #63402a;
    --cream: #ece1b5;
    --panel-line: #bdbdbd;
    --dash-line: #dedede;
    --ink: #2b2b2b;
    --white: #ffffff;
  }
  * { box-sizing: border-box; margin: 0; padding: 0; }
  html, body { width: 1200px; height: 1000px; overflow: hidden; background: var(--white); }
  body { font-family: "Arvo", Georgia, serif; color: var(--ink); }

  .canvas { position: relative; width: 1200px; height: 1000px; }

  .pouch {
    position: absolute; top: 76px; width: 554px; height: 846px;
    border: 1px solid var(--panel-line); background: var(--white); overflow: hidden;
  }
  .pouch--front { left: 26px; }
  .pouch--back { left: 620px; }

  .hang-hole {
    position: absolute; top: 116px; width: 11px; height: 11px;
    border: 1px solid #555; border-radius: 50%; background: var(--white);
  }

  .seal-dash {
    position: absolute; left: 34px; top: 110px; width: 479px; height: 12px;
    border: 1px dashed var(--dash-line); border-radius: 6px;
  }

  /* Front */
  .claim-script {
    position: absolute; left: 0; width: 100%; top: 6px; height: 70px; text-align: center;
    font-family: "Sacramento", cursive; font-size: 88px; line-height: 1;
    color: var(--cream); letter-spacing: 1px; white-space: nowrap;
  }
  .ingredient-line {
    position: absolute; left: 0; width: 100%; top: 80px; text-align: center;
    font-weight: 700; font-size: 20.5px; line-height: 24px; color: var(--bark-brown);
  }
  .ingredient-line .sep { font-weight: 400; margin: 0 2px; }

  .front-band { position: absolute; left: 0; top: 0; }

  .brand-mark {
    position: absolute; left: 0; width: 100%; text-align: center;
  }
  .brand-mark .dot {
    display: block; margin: 0 auto 10px; border-radius: 50%; background: var(--leaf-green);
  }
  .brand-mark .name {
    font-weight: 700; color: var(--bark-brown); line-height: 1.1;
  }
  .pouch--front .brand-mark { top: 150px; }
  .pouch--front .brand-mark .dot { width: 62px; height: 62px; }
  .pouch--front .brand-mark .name { font-size: 27px; }
  .pouch--back .brand-mark { top: 150px; }
  .pouch--back .brand-mark .dot { width: 40px; height: 40px; margin-bottom: 8px; }
  .pouch--back .brand-mark .name { font-size: 17px; }

  .flavour-line {
    position: absolute; left: 0; width: 100%; top: 296px; text-align: center;
    font-weight: 700; font-size: 41px; color: var(--bark-brown); letter-spacing: 1px;
  }
  .product-title { position: absolute; left: 0; top: 0; }
  .product-title text { font-family: "Arvo", Georgia, serif; font-weight: 700; fill: var(--white); }

  .product-window { position: absolute; left: 0; top: 472px; width: 554px; height: 316px;
    background: linear-gradient(90deg, #d6d6d6 0%, #f4f4f4 4%, #ffffff 8%, #ffffff 92%, #f1f1f1 96%, #d3d3d3 100%);
  }
  .product-window .treats {
    position: absolute; left: 54px; top: 0; width: 448px; height: 316px;
    background: radial-gradient(ellipse at 40% 45%, #f2d7a6 0%, #e0b574 45%, #c98a45 80%, #b4743a 100%);
  }

  .net-weight {
    position: absolute; left: 0; bottom: 0; width: 100%; height: 58px;
    background: var(--forest-green); color: var(--white);
    font-weight: 700; font-size: 15px; letter-spacing: 0.5px;
    display: flex; align-items: center; justify-content: center;
  }

  /* Back */
  .back-flavour {
    position: absolute; left: 0; width: 100%; top: 29px; text-align: center;
    font-weight: 700; font-size: 15px; color: var(--bark-brown); letter-spacing: 0.5px;
  }
  .back-product {
    position: absolute; left: 0; width: 100%; top: 50px; text-align: center;
    font-weight: 700; font-size: 21px; color: var(--leaf-green); letter-spacing: 0.8px;
  }
  .side-stripes { position: absolute; top: 252px; width: 71px; height: 438px; }
  .side-stripes--left { left: 0; }
  .side-stripes--right { right: 0; }

  .our-story {
    position: absolute; left: 94px; top: 250px; width: 382px;
    font-size: 13.4px; line-height: 21.3px; color: var(--ink);
  }
  .our-story p + p { margin-top: 21.3px; }

  .compost-guide {
    position: absolute; left: 0; bottom: 0; width: 100%; height: 156px;
    background: var(--forest-green); color: var(--white);
  }
  .compost-guide h2 {
    position: absolute; left: 0; width: 100%; top: 14px; text-align: center;
    font-size: 14.5px; font-weight: 700; letter-spacing: 0.8px;
  }
  .compost-step { position: absolute; top: 48px; display: flex; gap: 7px; }
  .compost-step--one { left: 43px; }
  .compost-step--two { left: 193px; }
  .compost-step--three { left: 342px; }
  .compost-step .step-art {
    width: 67px; height: 77px; border-radius: 2px; flex: none;
  }
  .compost-step--one .step-art { background: linear-gradient(180deg, #eef1f3 0%, #cfdde6 55%, #bcd0dc 100%); }
  .compost-step--two .step-art { background: linear-gradient(180deg, #dfe9ee 0%, #4fae6a 45%, #3a2d24 100%); }
  .compost-step--three .step-art { background: linear-gradient(180deg, #dceaf2 0%, #e9eed8 45%, #3a2d24 100%); }
  .compost-step h3 { font-size: 11px; font-weight: 700; line-height: 12px; letter-spacing: 0.4px; }
  .compost-step p { font-size: 8.6px; line-height: 9.6px; margin-top: 5px; }
  .compost-step--one .step-copy { width: 72px; }
  .compost-step--two .step-copy { width: 76px; }
  .compost-step--three .step-copy { width: 102px; }
</style>
</head>
<body>
<main class="canvas">

  <section class="pouch pouch--front" aria-label="Front of pouch">
    <div class="claim-script">all natural</div>
    <p class="ingredient-line">ingredients<span class="sep">|</span>coconut oil<span class="sep">|</span>dill<span class="sep">|</span>sweet potato</p>
    <div class="seal-dash"></div>

    <svg class="front-band" width="554" height="480" viewBox="0 0 554 480" aria-hidden="true">
      <defs>
        <clipPath id="front-band-shape">
          <path d="M0,252 L148,208 C168,268 218,294 277,294 C336,294 386,268 406,208 L554,252 L554,472 L0,472 Z"/>
        </clipPath>
      </defs>
      <g clip-path="url(#front-band-shape)">
        <rect x="0" y="200" width="554" height="272" fill="var(--leaf-green)"/>
        <g fill="var(--stripe-green)">
          <rect x="38" y="200" width="4" height="272"/>
          <rect x="84" y="200" width="4" height="272"/>
          <rect x="124" y="200" width="4" height="272"/>
          <rect x="172" y="200" width="4" height="272"/>
          <rect x="220" y="200" width="4" height="272"/>
          <rect x="274" y="200" width="4" height="272"/>
          <rect x="326" y="200" width="4" height="272"/>
          <rect x="378" y="200" width="4" height="272"/>
          <rect x="424" y="200" width="4" height="272"/>
          <rect x="470" y="200" width="4" height="272"/>
          <rect x="514" y="200" width="4" height="272"/>
        </g>
      </g>
    </svg>

    <div class="brand-mark">
      <span class="dot"></span>
      <span class="name">Tailwag Pantry!</span>
    </div>

    <h1 class="flavour-line">MAPLE SAGE</h1>
    <svg class="product-title" width="554" height="472" viewBox="0 0 554 472" aria-label="Crunchy Bark-ley Bites">
      <defs>
        <path id="title-arc" d="M40,458 Q277,300 514,458"/>
      </defs>
      <text font-size="35" letter-spacing="1">
        <textPath href="#title-arc" startOffset="50%" text-anchor="middle">CRUNCHY BARK-LEY</textPath>
      </text>
      <text x="277" y="446" font-size="48" text-anchor="middle" letter-spacing="1">BITES</text>
    </svg>

    <div class="product-window">
      <div class="treats" role="img" aria-label="Photo of golden baked sweet potato treat strips seen through the bag window"></div>
    </div>

    <div class="net-weight">NET WT. 250g OPTIMIZED</div>
  </section>

  <section class="pouch pouch--back" aria-label="Back of pouch">
    <p class="back-flavour">MAPLE SAGE</p>
    <h2 class="back-product">CRUNCHY BARK-LEY BITES</h2>
    <div class="seal-dash"></div>

    <div class="brand-mark">
      <span class="dot"></span>
      <span class="name">Tailwag Pantry!</span>
    </div>

    <svg class="side-stripes side-stripes--left" viewBox="0 0 71 438" preserveAspectRatio="none" aria-hidden="true">
      <rect width="71" height="438" fill="var(--leaf-green)"/>
      <rect x="22" width="4" height="438" fill="var(--stripe-green)"/>
      <rect x="50" width="4" height="438" fill="var(--stripe-green)"/>
    </svg>
    <svg class="side-stripes side-stripes--right" viewBox="0 0 71 438" preserveAspectRatio="none" aria-hidden="true">
      <rect width="71" height="438" fill="var(--leaf-green)"/>
      <rect x="28" width="4" height="438" fill="var(--stripe-green)"/>
      <rect x="54" width="4" height="438" fill="var(--stripe-green)"/>
    </svg>

    <div class="our-story">
      <p>We are a local Cedarbrook pet treat company that emerged from an unwavering passion for supporting the pet community, as well as providing pets a healthy alternative with just a few or less ingredients. We always use fresh ingredients and we make each bag with love, just as though we are creating it for our children because--lets face it--our pets are our children. Further, at Tailwag Pantry, we are committed to using a portion of our product proceeds to help local animal shelters. By doing so, we are creating a better world for all of our best friends.</p>
      <p>Our company was built on the foundation of giving back. We focus on ensuring that our donations aid rescues, shelters, charities and more to guarantee that our furry friends are taken off the streets and placed in loving homes where they receive food, medication and the care that they so need and deserve.</p>
    </div>

    <div class="compost-guide">
      <h2>HOW TO COMPOST YOUR BAG IN 2 SIMPLE STEPS</h2>
      <div class="compost-step compost-step--one">
        <div class="step-art" role="img" aria-label="Illustration of scissors cutting the zipper track off the top of the bag"></div>
        <div class="step-copy">
          <h3>STEP 1</h3>
          <p>Cut-off top zipper and track from bag and recycle in blue bin.</p>
        </div>
      </div>
      <div class="compost-step compost-step--two">
        <div class="step-art" role="img" aria-label="Illustration of the bag going into a green compost bin"></div>
        <div class="step-copy">
          <h3>STEP 2</h3>
          <p>Dispose bag in green bin for composting.</p>
        </div>
      </div>
      <div class="compost-step compost-step--three">
        <div class="step-art" role="img" aria-label="Illustration of the bag in soil under sun and rain"></div>
        <div class="step-copy">
          <h3>FOR BEST RESULTS IN COMPOSTING</h3>
          <p>Heat, Moisture, and Microbes.</p>
        </div>
      </div>
    </div>
  </section>

  <span class="hang-hole" style="left:21px"></span>
  <span class="hang-hole" style="left:574px"></span>
  <span class="hang-hole" style="left:615px"></span>
  <span class="hang-hole" style="left:1168px"></span>

</main>
</body>
</html>
```